" O INSTITUTO TERAVUNDA foi idealizado a partir de um ideal de auxílio humanitário a famílias (com algum idoso) com condições de sobrevivência comprometidas devido a problemas de doença, seja ela física; psicológica ou mesmo social. “ Teravunda” significa “dono da coragem” e, apesar de seu principal mantenedor ser uma casa de culto de matriz africana (Dasilore Mitaku Fenjo Arupe),o Centro Cultural visa atender a famílias com idosos que estejam desestruturadas, devido a algum tipo de doença, indiferente a visão política, religiosa e/ou cultural. Acreditamos que o idoso incluído num contexto familiar, ou mesmo num asilo, não deve ser culpado por qualquer atitude de sua juventude. Quem de nós, em idade de produção e escolhas pode garantir estar tomando decisões acertadas para seu futuro? Normalmente são as doenças que comprometem o bem estar social: vícios em bebidas e/ou drogas; doenças patológicas e/ou psicológicas ou mesmo “doenças sociais” desestruturam as relações interpessoais afastando os idosos da realidade. "

```html
<!DOCTYPE html>
<html lang="pt-BR">
<head>
<meta charset="UTF-8">
<title>Instituto Teravunda</title>
<link rel="stylesheet" href="https://fonts.googleapis.com/css2?family=Raleway:wght@400;500;600;700;800&display=swap">
<style>
  :root{
    --page-bg:#f1f1f1;
    --orange:#e8541e;
    --white:#ffffff;
    --nav-text:#5a5a5a;
    --logo:#d9491c;
    --hero-top:#a9ae98;
    --hero-bottom:#7d8a55;
    --hero-shade:rgba(0,0,0,0.3);
  }
  *{box-sizing:border-box;margin:0;padding:0}
  html,body{width:1200px;height:1200px;overflow:hidden}
  body{background:var(--page-bg);font-family:"Raleway",sans-serif;display:flex;align-items:center}
  .site{width:1200px;height:672px;background:var(--white);display:flex;flex-direction:column}
  .topbar{height:62px;background:var(--orange);color:var(--white);display:flex;align-items:center;justify-content:space-between;padding:0 72px;font-size:14px;font-weight:600}
  .topbar__item{display:flex;align-items:center;gap:8px;white-space:nowrap}
  .topbar__sep{width:1px;height:22px;background:rgba(255,255,255,0.55)}
  .nav{height:98px;display:flex;align-items:center;justify-content:space-between;padding:0 72px 0 68px}
  .brand{display:flex;align-items:center;gap:12px}
  .brand__dot{width:34px;height:34px;border-radius:50%;background:var(--logo)}
  .brand__name{color:var(--logo);font-weight:700;font-size:26px;line-height:1}
  .menu{display:flex;gap:42px;list-style:none;font-size:17px;font-weight:500;color:var(--nav-text);letter-spacing:.3px}
  .hero{position:relative;flex:1;overflow:hidden}
  .hero__photo{position:absolute;inset:0;background:linear-gradient(180deg,var(--hero-top) 0%,var(--hero-bottom) 100%)}
  .hero__content{position:absolute;left:262px;top:240px;width:540px;color:var(--white)}
  .hero__title{font-size:32px;font-weight:800;line-height:1.1;text-shadow:0 1px 3px var(--hero-shade)}
  .hero__text{margin-top:8px;font-size:14px;line-height:1.4;font-weight:500;text-shadow:0 1px 2px var(--hero-shade)}
  .hero__button{position:absolute;left:452px;top:352px;width:156px;height:36px;border-radius:4px;background:var(--orange);color:var(--white);font-size:16px;font-weight:600;display:flex;align-items:center;justify-content:center}
  .hero__dots{position:absolute;left:0;right:0;bottom:28px;display:flex;justify-content:center;gap:9px}
  .hero__dots span{width:12px;height:12px;border-radius:50%;background:var(--white)}
</style>
</head>
<body>
  <div class="site">
    <header class="topbar">
      <span class="topbar__item">O que está procurando?</span>
      <span class="topbar__sep"></span>
      <span class="topbar__item">Horário de funcionamento: Seg. a Sexta das 08:00 às 18:00</span>
      <span class="topbar__sep"></span>
      <span class="topbar__item">contato@teravunda.org</span>
      <span class="topbar__sep"></span>
      <span class="topbar__item">
        <svg width="20" height="20" viewBox="0 0 24 24" aria-hidden="true"><path fill="#fff" d="M6.6 10.8a15 15 0 0 0 6.6 6.6l2.2-2.2a1 1 0 0 1 1-.25 11.4 11.4 0 0 0 3.6.57 1 1 0 0 1 1 1V20a1 1 0 0 1-1 1A17 17 0 0 1 3 4a1 1 0 0 1 1-1h3.5a1 1 0 0 1 1 1c0 1.25.2 2.45.57 3.57a1 1 0 0 1-.25 1z"/></svg>
        (xx) xxxx - xxxx (xx) xxxx - xxxx
      </span>
    </header>
    <nav class="nav">
      <div class="brand"><span class="brand__dot"></span><span class="brand__name">Instituto Teravunda</span></div>
      <ul class="menu">
        <li>HOME</li><li>QUEM SOMOS</li><li>PARCEIROS</li><li>NEWS</li><li>CONTATO</li>
      </ul>
    </nav>
    <section class="hero">
      <div class="hero__photo" role="img" aria-label="Fotografia de um casal de idosos sentados num banco de madeira em um parque"></div>
      <div class="hero__content">
        <h1 class="hero__title">TERAVUNDA “dono da coragem”</h1>
        <p class="hero__text">TERAVUNDA é um espaço de integração e cuidado da pessoa idosa e tem a finalidade de proporcionar experiências e fortalecer laços, além de oferecer cuidados de higiene e alimentação.</p>
      </div>
      <div class="hero__button">Buscar</div>
      <div class="hero__dots"><span></span><span></span><span></span><span></span></div>
    </section>
  </div>
</body>
</html>
```